Modern brochure by Lawyers, for modern clients

It'sa "News" for their clients. Attached you can find the current News without design. It must be elegant but very attractive and modern. Their web site is http://www.montalbanyasociados.cl/ Their expertise is labor and employment practice area. It must be in editable format so that lawyers can write the news in a template with this corporate design.

Target Market(s)

Big Companies

Font styles to use
Sans Serif

Colors
0255a3
474747

Requirements
Nice to have
• Legal Pictures and only a little of yellow. One touch! It must be in editable format so that lawyers can write the news in a template with this corporate design.

```html
<!DOCTYPE html>
<html lang="es">
<head>
<meta charset="utf-8">
<title>Montalbán Asociados Abogados · Noticias</title>
<link rel="stylesheet" href="https://fonts.googleapis.com/css2?family=Josefin+Sans:wght@300&family=Lato:wght@300;400;700&display=swap">
<style>
  :root {
    --navy: #3b5574;
    --navy-deep: #2f4565;
    --sky-top: #2f5fc4;
    --sky-bottom: #4f86d9;
    --ink: #2e2e2e;
    --brand-ink: #2e4366;
    --link: #2b4a7c;
    --paper: #ffffff;
    --stage: #e9ebee;
  }
  * { margin: 0; padding: 0; box-sizing: border-box; }
  html, body { width: 1200px; height: 1200px; overflow: hidden; background: var(--stage); }
  .newsletter {
    position: absolute; left: 180px; top: 6px;
    width: 840px; height: 1188px;
    background: var(--paper);
    font-family: "Lato", sans-serif;
    color: var(--ink);
    overflow: hidden;
  }
  .masthead {
    position: absolute; left: 0; top: 0; width: 100%; height: 72px;
    background: var(--navy);
  }
  .masthead__date {
    position: absolute; right: 48px; top: 44px;
    color: #fff; font-size: 17.5px; font-weight: 400;
  }
  .hero {
    position: absolute; left: 0; top: 83px; width: 100%; height: 363px;
    background: linear-gradient(160deg, var(--sky-top), var(--sky-bottom));
  }
  .brand {
    position: absolute; left: 0; top: 430px; width: 100%; height: 200px;
  }
  .brand__name {
    position: absolute; left: 219px; top: 72px;
    font-family: "Josefin Sans", sans-serif; font-weight: 300;
    color: var(--brand-ink); line-height: 1;
  }
  .brand__name-main { display: block; font-size: 62px; letter-spacing: 4px; }
  .brand__name-sub { display: block; font-size: 40px; letter-spacing: 1px; margin-top: 10px; }
  .letter {
    position: absolute; left: 94px; top: 606px; width: 652px;
    font-size: 15px; font-weight: 300; line-height: 20.3px;
    text-align: justify;
  }
  .letter p { margin-bottom: 20px; }
  .letter__highlight { font-weight: 700; color: #111; }
  .letter__highlight a { color: var(--link); text-decoration: underline; font-weight: 400; }
  .letter__closing { margin-bottom: 10px !important; }
  .letter__signature { color: var(--brand-ink); font-weight: 400; font-size: 15.5px; }
  .footer {
    position: absolute; left: 0; bottom: 0; width: 100%; height: 34px;
    background: var(--navy);
    display: flex; justify-content: space-between; align-items: center;
    padding: 0 40px;
    color: #fff; font-size: 11.5px; font-weight: 400;
  }
</style>
</head>
<body>
<article class="newsletter">
  <header class="masthead">
    <p class="masthead__date">Santiago, 25 de julio de 2018</p>
  </header>

  <div class="hero" role="img" aria-label="Fotografía de un edificio corporativo de vidrio azul contra el cielo"></div>

  <div class="brand">
    <svg width="840" height="200" viewBox="0 0 840 200" style="position:absolute;left:0;top:0">
      <path d="M0 16 H48 C66 16 70 30 70 50 C70 100 100 128 138 128 C176 128 204 100 210 60 C214 30 224 16 250 16 H840 V200 H0 Z" fill="#fff"/>
      <circle cx="138" cy="70" r="52" fill="#3b5574" stroke="#5a88d6" stroke-width="6"/>
      <rect x="773" y="80" width="8" height="28" fill="#e3ecf3"/>
      <rect x="773" y="108" width="8" height="28" fill="#c5d4e0"/>
      <rect x="773" y="136" width="8" height="28" fill="#8ea3b8"/>
      <rect x="773" y="164" width="8" height="28" fill="#3b5574"/>
    </svg>
    <p class="brand__name">
      <span class="brand__name-main">MONTALBÁN</span>
      <span class="brand__name-sub">ASOCIADOS ABOGADOS</span>
    </p>
  </div>

  <section class="letter">
    <p>Estimados,</p>
    <p>Por medio del presente, les damos a conocer el Dictamen Ordinario N° 3826-031, emitido por la Dirección del Trabajo el pasado 20 de julio, relativo a los “beneficios históricos”.</p>
    <p>Estos fueron definidos en su oportunidad por este organismo como “…aquellos beneficios que se han otorgado desde siempre…” por parte del empleador.</p>
    <p>A partir de este Dictamen, el cual reconsidera el criterio del anterior Director del Trabajo, los beneficios históricos vuelven a ser patrimonio de la empresa y de los trabajadores que los han recibido, dejando de serlo de la organización sindical y de sus socios beneficiados por el solo hecho de haberse “replicado” en un instrumento colectivo durante una negociación.</p>
    <p>Por último, el Dictamen en comento aclara que si un “beneficio histórico” se incrementa de manera real y efectiva producto de una negociación colectiva, únicamente dicho incremento se entenderá originado en el respectivo instrumento colectivo, y en consecuencia, objeto de una posible extensión en el evento de que ésta se haya acordado durante la negociación.</p>
    <p class="letter__highlight">Para mayor análisis de lo resuelto por la Dirección del Trabajo, se puede revisar el Dictámen en comento <a href="http://www.montalbanyasociados.cl/">haciendo click aquí</a></p>
    <p class="letter__closing">Sin otro particular, saluda atentamente a ustedes,</p>
    <p class="letter__signature">Montalbán y Asociados Abogados<br>oficina@montalbanyasociados.cl</p>
  </section>

  <footer class="footer">
    <span>Av. Los Olmos 4120, piso 3, Las Condes</span>
    <span>T +56 2 229876510</span>
    <span>E oficina@montalbanyasociados.cl</span>
    <span>W www.montalbanyasociados.cl</span>
  </footer>
</article>
</body>
</html>
```